Lens Harbor Teutonia Website - Photography and Films

We are looking for a design that expresses the friendly, open nature of our company Lens Harbor Teutonia, yet at the same time is professional looking and functional.

Lens Harbor Teutonia is a B2B focused operation that hires out multi-lingual camera crews (and equipment) throughout Germany and Europe. We also produce tv features and coporate films. Our unique selling point is that we are native English speakers who can communicate with our international clients (usually British or American) and organise the logistics of shooting in foreign countries.

For content inspiration, see our current website: http://www.lensharborteutonia.com - however we want to move away from the very simple structure of this site and move towards a layout that displays and allows for frequently updated content (e.g. in the form of a blog).

Here is an example of the kind of clean look we like:
http://www.qrvpixelarchive.com/archive/main/reelsqrv.do#reel=48213760

Please keep within the following specifications:
- We wish to keep our logo (grey/white, font: Glypha) and our company colour red (#C40A0A) as they are.
- Maximum Width 960px, on a large browser-window the design should be centred
- Easily readable font sizes with good contrast
- Provide your design in PSD file format
- Our logo should be graphically displayed in the top left of the header.
- The design should allow space for a video.
- The page should have a clearly recognisable end in the form of a footer.

The following menu items need to be clearly arranged so the viewer is not overwhelmed or confused:
About
Services - Crews / Corporate Shoots / Webcasts / Production Arm / Legal Videography
Recent Productions
Blog
Testimonials
Get a Quote
Contact
Film Library
Showreel
Events
Film Location Guide - Frankfurt / Cologne / Zurich / Helsinki / Amsterdam / London / Paris / Rome / Brussels / Berlin / Munich
Updates

Reason: Hi - thanks very much for your interest in our design project.  We are extending this auction because we haven't had enough time to really focus on the desigs and provide immediate feedback to designers.  We will try to provide timely feedback and are giving you more time to make any adjustments to your designs etc.
Thanks!
Marla

Target Market(s)

Our target customers are males and females between 25 and 55 years (mostly British and American). More important than their demographic though, is their occupation - they are largely communication and design savvy individuals belonging to one of the following three categories: 1)Broadcasters (usually producers for example from the QRV or Horizon Vista TV seeking trustworthy, affordable crews for their foreign shoots).

2) Video Production Companies (seeking a trustworthy, affordable partner company to provide the crews for their own corporate clients).

3) Corporate Communications Specialists (seeking professional producers and crews to facilitate production of company videos or filming of events).

Industry/Entity Type

Camera

Requirements
Must have
• A fresh clean appearance with good use of white space.
Should not have
• Avoid dark heavy colours and designs.
• Avoid designs that would be impractical and could potentially take a long time to load.

```html
<!DOCTYPE html>
<html lang="en">
<head>
<meta charset="utf-8">
<title>Lens Harbor Teutonia – About</title>
<link href="https://fonts.googleapis.com/css2?family=Arimo:wght@400;700&display=swap" rel="stylesheet">
<style>
  :root {
    --brand-red: #c40a0a;
    --ink: #2b2b2b;
    --ink-soft: #555;
    --panel: #ffffff;
    --page-top: #f4f4f4;
    --page-bottom: #e4e4e4;
    --band-grey: #d3d3cc;
    --player-dark: #1f1f1f;
  }
  * { box-sizing: border-box; margin: 0; padding: 0; }
  html, body { width: 1200px; height: 900px; overflow: hidden; }
  body {
    position: relative;
    font-family: "Arimo", Arial, sans-serif;
    color: var(--ink);
    background: linear-gradient(to bottom, var(--page-top) 0%, #fafafa 60%, var(--page-bottom) 100%);
  }
  .page-panel {
    position: absolute; left: 98px; top: 0; width: 1004px; height: 835px;
    background: var(--panel);
    border-radius: 0 0 30px 30px;
    box-shadow: 0 2px 8px rgba(0,0,0,0.08);
  }
  .header-band { position: absolute; left: 0; top: 0; width: 1200px; height: 200px; }
  .brand-name {
    position: absolute; right: 135px; top: 30px;
    font-size: 56px; line-height: 60px; font-weight: 700; color: #fff; letter-spacing: -1.5px;
    text-transform: lowercase; white-space: nowrap;
  }
  .search-box {
    position: absolute; left: 680px; top: 138px; width: 350px; height: 54px;
    background: #f1f1f1; border-radius: 16px;
    box-shadow: 0 1px 4px rgba(0,0,0,0.25);
  }
  .search-field {
    position: absolute; left: 10px; top: 8px; width: 332px; height: 42px;
    border: 3px solid var(--brand-red); border-radius: 12px; background: #fff; overflow: hidden;
  }
  .search-field span {
    position: absolute; left: 14px; top: 11px;
    font-size: 18px; font-style: italic; color: #aaa;
  }
  .search-button {
    position: absolute; right: 0; top: 0; width: 52px; height: 36px;
    background: var(--brand-red);
  }
  .main-nav {
    position: absolute; left: 107px; top: 211px; display: flex; align-items: center;
    font-size: 16.5px; color: #111; white-space: nowrap;
  }
  .nav-icon {
    width: 27px; height: 27px; background: var(--brand-red); border-radius: 5px; margin-right: 5px;
    position: relative;
  }
  .nav-icon::after {
    content: ""; position: absolute; left: 9px; top: 7px;
    border-left: 11px solid #fff; border-top: 6px solid transparent; border-bottom: 6px solid transparent;
  }
  .main-nav a { color: inherit; text-decoration: none; }
  .main-nav .current { color: var(--brand-red); }
  .main-nav .sep { margin: 0 5px; }
  .main-nav .sep.red { color: var(--brand-red); margin: 0 7px 0 10px; }
  .video-player { position: absolute; left: 113px; top: 252px; width: 470px; height: 261px; }
  .video-frame {
    width: 470px; height: 232px;
    background: linear-gradient(to bottom, #dfe6ec 0%, #b9c4cc 25%, #3a4030 45%, #5f6a6c 65%, #2c3320 100%);
    position: relative;
  }
  .play-overlay {
    position: absolute; left: 209px; top: 90px; width: 52px; height: 52px; border-radius: 50%;
    background: rgba(60,60,60,0.75);
  }
  .play-overlay::after {
    content: ""; position: absolute; left: 20px; top: 14px;
    border-left: 20px solid #eee; border-top: 12px solid transparent; border-bottom: 12px solid transparent;
  }
  .video-controls { width: 470px; height: 29px; background: linear-gradient(#3a3a3a, var(--player-dark)); }
  .feature-photo {
    position: absolute; left: 601px; top: 252px; width: 319px; height: 174px;
    background: linear-gradient(135deg, #e4e4e4 0%, #cfcfcf 50%, #d9c9a4 100%);
  }
  .feature-date {
    position: absolute; left: 975px; top: 265px; padding-left: 8px;
    border-left: 3px solid #bbb; font-size: 10px; word-spacing: 4px; color: #222;
  }
  .feature-summary {
    position: absolute; left: 930px; top: 325px; width: 146px;
    font-size: 10px; line-height: 12px; text-align: justify; color: #222;
  }
  .thumb-strip { position: absolute; left: 601px; top: 439px; width: 479px; height: 74px; display: flex; }
  .strip-arrow { width: 9px; height: 74px; background: var(--brand-red); position: relative; }
  .strip-arrow::after {
    content: ""; position: absolute; top: 32px; left: 2px;
    border-top: 5px solid transparent; border-bottom: 5px solid transparent;
  }
  .strip-arrow.prev::after { border-right: 5px solid #fff; }
  .strip-arrow.next::after { border-left: 5px solid #fff; }
  .thumbs { flex: 1; display: flex; gap: 4px; padding: 0 3px; overflow: hidden; }
  .thumb { flex: 0 0 97px; height: 74px; }
  .thumb.t1 { background: linear-gradient(135deg, #ddd, #c9b48a); }
  .thumb.t2 { background: linear-gradient(135deg, #c8c8c8, #8d8d8d); }
  .thumb.t3 { background: linear-gradient(180deg, #dfe6ee, #e4c64a 60%, #bbb); }
  .thumb.t4 { background: linear-gradient(135deg, #b5b5b5, #7a7a7a); }
  .thumb.t5 { flex: 1 1 auto; background: linear-gradient(135deg, #aaa, #777); }
  .news-tab {
    position: absolute; left: 107px; top: 524px; width: 180px; height: 24px;
    background: var(--band-grey); font-size: 12px; padding: 5px 0 0 20px; color: #333;
  }
  .news-tab::before {
    content: ""; position: absolute; left: 7px; top: 7px;
    border-left: 8px solid #fff; border-top: 5px solid transparent; border-bottom: 5px solid transparent;
  }
  .news-tab .label { text-decoration: underline; }
  .news-tab .light { color: #fff; }
  .news-band { position: absolute; left: 297px; top: 524px; width: 798px; height: 24px; background: var(--band-grey); }
  .about-copy {
    position: absolute; left: 114px; top: 561px; width: 960px;
    font-size: 12px; line-height: 14.5px; color: var(--ink); letter-spacing: 0.15px;
  }
  .about-copy p { margin-bottom: 14.5px; }
  .service-list { list-style: none; margin: 0 0 14.5px 21px; }
  .service-list li { position: relative; padding-left: 15px; }
  .service-list li::before {
    content: ""; position: absolute; left: 0; top: 2px; width: 11px; height: 11px;
    background: var(--brand-red); border-radius: 2px;
  }
  .service-list li::after {
    content: ""; position: absolute; left: 4px; top: 5px;
    border-left: 5px solid #fff; border-top: 3px solid transparent; border-bottom: 3px solid transparent;
  }
  .site-footer {
    position: absolute; left: 498px; top: 859px; padding-left: 13px;
    border-left: 3px solid #c8c8c8; font-size: 10px; line-height: 12px; color: #666; word-spacing: 3px;
  }
</style>
</head>
<body>
  <div class="page-panel"></div>

  <svg class="header-band" width="1200" height="200" viewBox="0 0 1200 200" aria-hidden="true">
    <polygon points="20,0 1200,0 1100,180 680,180" fill="#c40a0a"/>
  </svg>

  <div class="brand-name">lensharborteutonia</div>

  <div class="search-box">
    <div class="search-field">
      <span>Search...</span>
      <div class="search-button">
        <svg width="52" height="36" viewBox="0 0 52 36" aria-hidden="true">
          <circle cx="21" cy="16" r="9" fill="none" stroke="#fff" stroke-width="2.5"/>
          <line x1="28" y1="22" x2="38" y2="30" stroke="#fff" stroke-width="4" stroke-linecap="round"/>
        </svg>
      </div>
    </div>
  </div>

  <nav class="main-nav">
    <span class="nav-icon"></span>
    <a class="current" href="#">About</a><span class="sep red">|</span>
    <a href="#">Services</a><span class="sep">|</span>
    <a href="#">Recent Productions</a><span class="sep">|</span>
    <a href="#">Blog</a><span class="sep">|</span>
    <a href="#">Testimonials</a><span class="sep">|</span>
    <a href="#">Get a Quote</a><span class="sep">|</span>
    <a href="#">Contact</a><span class="sep">|</span>
    <a href="#">Film Library</a><span class="sep">|</span>
    <a href="#">Showreel</a><span class="sep">|</span>
    <a href="#">Events</a>
  </nav>

  <div class="video-player">
    <div class="video-frame" role="img" aria-label="Video still of a misty lake with reeds and a forest line at sunrise">
      <div class="play-overlay"></div>
    </div>
    <svg class="video-controls" width="470" height="29" viewBox="0 0 470 29" aria-hidden="true">
      <circle cx="21" cy="15" r="9" fill="#555"/>
      <polygon points="18,10 26,15 18,20" fill="#ddd"/>
      <rect x="38" y="11" width="226" height="7" rx="3.5" fill="#111"/>
      <circle cx="43" cy="14.5" r="5" fill="#eee"/>
      <rect x="272" y="7" width="80" height="15" rx="7" fill="#111"/>
      <text x="279" y="18" font-family="Arimo, Arial, sans-serif" font-size="9" fill="#fff">00:00 /</text>
      <text x="312" y="18" font-family="Arimo, Arial, sans-serif" font-size="9" fill="#c40a0a">00:00</text>
      <polygon points="362,12 366,12 370,8 370,21 366,17 362,17" fill="#ddd"/>
      <rect x="376" y="11" width="42" height="7" rx="3.5" fill="#111"/>
      <circle cx="401" cy="14.5" r="5" fill="#eee"/>
      <rect x="429" y="8" width="13" height="13" rx="2" fill="#555"/>
      <rect x="446" y="8" width="13" height="13" rx="2" fill="#555"/>
      <rect x="449" y="11" width="7" height="1.5" fill="#ddd"/>
      <rect x="449" y="14" width="7" height="1.5" fill="#ddd"/>
      <rect x="449" y="17" width="7" height="1.5" fill="#ddd"/>
    </svg>
  </div>

  <div class="feature-photo" role="img" aria-label="Photo of a client's printed company sign at a shoot location"></div>
  <div class="feature-date">October 27, 2010</div>
  <p class="feature-summary">California based Arcline productions asked us to film testimonials and B roll for a major client that produces industrial chips, Corvantix. We shot at Dellmore in Holland and Brightwave Telecom in Munich</p>

  <div class="thumb-strip">
    <div class="strip-arrow prev"></div>
    <div class="thumbs">
      <div class="thumb t1" role="img" aria-label="Thumbnail of a company sign"></div>
      <div class="thumb t2" role="img" aria-label="Thumbnail of a camera crew filming an interview"></div>
      <div class="thumb t3" role="img" aria-label="Thumbnail of delivery vans parked outdoors"></div>
      <div class="thumb t4" role="img" aria-label="Thumbnail of a cameraman filming a sports car"></div>
      <div class="thumb t5" role="img" aria-label="Thumbnail of a crew on location"></div>
    </div>
    <div class="strip-arrow next"></div>
  </div>

  <div class="news-tab"><span class="label"><span class="light">news</span>entries</span></div>
  <div class="news-band"></div>

  <main class="about-copy">
    <p>We set up Lens Harbor Teutonia to meet the demands of a growing number of TV-producers whose working language is English. This is our Passion! Why else would we keep doing it for over 30 years!</p>
    <p>As a producer, you’re bound to have great ideas…but how do you make them a reality in a country where you can’t speak the language? Partner with us!</p>
    <p>We are native English speakers so nothing gets lost in translation. We’ll catch hold of your vision, and with local know-how, we’ll make it happen.</p>
    <p>No job is too big, too small, too hard, too far away, or too urgent. Try us!</p>
    <ul class="service-list">
      <li>We provide camera crews and facilities throughout Germany and Europe</li>
      <li>We shoot in both PAL and NTSC</li>
      <li>We edit either in-studio or on the move and we transfer urgent footage via FTP or SNG</li>
      <li>We are on call 24/7</li>
    </ul>
    <p>To make a no obligation enquiry about any of our services, please call our Frankfurt Headquarters: +49-69-472615 (Toll free from the USA 1-866-555-0142) or click here to get a quote.</p>
  </main>

  <footer class="site-footer">
    c/o Halloway Films • Lindenweg 12 • 60311 Frankfurt/Main • Germany • info@lens-harbor-teutonia.com<br>
    Tel.: +49-69-472615 • Toll free from the USA 1-866-555-0142<br>
    Disclaimer
  </footer>
</body>
</html>
```